New web design for a service provider in the medical field

We are looking for a new design for our website. We are a company that repairs and sells medical endoscopes. Our customers include doctors and hospitals. Our current website can be found at https://lumenfix.example/en/lumenfix-english.
We need a new web design (without programming) for the following 3 pages:
-Startpage https://lumenfix.example/en/lumenfix-english/
-Used endoscopes https://lumenfix.example/en/used-endoscopes/
-Purchase https://lumenfix.example/en/purchase/
The design should be modern and stylish.
The blue color of the logo should be reflected on the page, but not too intrusive.
I have uploaded the images from the header. If more images are needed, let me know and I will upload them.

Target Market(s)
Doctors and hospitals

```html
<!DOCTYPE html>
<html lang="en">
<head>
<meta charset="utf-8">
<title>LumenFix – Endoscope Repair &amp; Sale</title>
<link href="https://fonts.googleapis.com/css2?family=Mulish:wght@400;600;700;800&display=swap" rel="stylesheet">
<style>
:root{
  --blue:#29a8e0;
  --blue-deep:#17679a;
  --blue-band:#1c78ad;
  --ink:#22272b;
  --muted:#6b7378;
  --light:#f3f5f7;
  --footer:#1f2a31;
  --orbica:#1f6fc9;
  --pentrel:#e0243f;
  --fujora:#262626;
}
*{box-sizing:border-box;margin:0;padding:0}
html,body{width:1200px;height:4428px;overflow:hidden}
body{font-family:"Mulish",Arial,sans-serif;color:var(--ink);background:#fff;position:relative}
.abs{position:absolute}
.btn{position:absolute;display:flex;align-items:center;justify-content:center;background:var(--blue);color:#fff;font-size:10px;font-weight:700;letter-spacing:.5px;text-transform:uppercase;height:30px}

/* top bar */
.topbar{position:absolute;top:0;left:0;width:1200px;height:21px;background:var(--blue);color:#fff;font-size:9px}
.topbar .links{position:absolute;left:129px;top:5px;letter-spacing:.3px}
.topbar .links span{margin-right:14px}
.topbar .contact{position:absolute;right:131px;top:5px}
.topbar .contact span{margin-left:18px}

/* nav */
.nav{position:absolute;top:21px;left:0;width:1200px;height:60px;background:#fff}
.nav .brand{position:absolute;left:136px;top:22px;font-size:14px;font-weight:800;color:var(--blue-deep)}
.nav .menu{position:absolute;right:129px;top:25px;display:flex;gap:32px;font-size:9px;font-weight:600;text-transform:uppercase;color:var(--ink)}
.nav .menu .active{color:var(--blue)}

/* hero */
.hero{position:absolute;top:81px;left:0;width:1200px;height:500px}
.hero-photo{position:absolute;inset:0;background:linear-gradient(120deg,#2c6f93 0%,#3e83a6 45%,#5b94b2 75%,#2b5f7f 100%)}
.hero .pre{position:absolute;left:129px;top:155px;color:#fff;font-size:20px}
.hero h1{position:absolute;left:129px;top:183px;color:#fff;font-size:40px;font-weight:400;line-height:47px}
.hero .btn{left:130px;top:300px;width:112px;height:30px}
.hero .mark{position:absolute;left:533px;top:200px;color:#fff;font-size:70px;font-weight:800}
.hero svg{position:absolute;left:0;bottom:0}

/* welcome */
.welcome-photo{position:absolute;left:129px;top:636px;width:423px;height:342px;border-radius:0 0 34px 0;background:linear-gradient(140deg,#e7ebee,#c9d0d5 60%,#aeb8bf)}
.kicker{font-size:14px;color:var(--ink)}
.welcome .kicker{position:absolute;left:608px;top:692px}
.welcome h2{position:absolute;left:608px;top:714px;font-size:30px;font-weight:600}
.welcome p{position:absolute;left:608px;top:780px;width:460px;font-size:12px;line-height:19px;color:var(--muted)}
.welcome .btn{left:609px;top:889px;width:111px}

/* blue band */
.band{position:absolute;top:1049px;left:0;width:1200px;height:448px;background:var(--blue-band);overflow:hidden}
.band-photo{position:absolute;right:0;top:0;width:600px;height:448px;background:linear-gradient(160deg,#e9ecee,#cfd4d8);clip-path:path("M120 0 L600 0 L600 448 L66 448 C 0 330 20 120 120 0 Z")}
.band .kicker{position:absolute;left:129px;top:73px;color:#fff;font-size:14px}
.band h2{position:absolute;left:129px;top:92px;color:#fff;font-size:34px;font-weight:600;line-height:38px}
.band .cause{position:absolute;left:129px;top:183px;color:#fff;font-size:15px;letter-spacing:.3px}
.band p{position:absolute;left:129px;top:232px;width:415px;color:#fff;font-size:12px;line-height:20px}
.band .btn{left:131px;top:345px;width:111px;background:var(--blue)}

/* cards */
.card{position:absolute;top:1568px;width:300px;height:240px;text-align:center;background:#fff}
.card.framed{border:1px solid #555}
.card.shadow{box-shadow:0 4px 18px rgba(0,0,0,.08)}
.card svg{margin-top:16px}
.card h3{font-size:16px;font-weight:600;margin-top:8px}
.card .sub{font-size:11px;color:var(--blue);margin-top:2px}
.card p{font-size:10px;line-height:16px;color:var(--muted);width:250px;margin:14px auto 0}
.card .btn{left:84px;top:180px;width:132px}

/* decision */
.decision{position:absolute;top:1877px;left:0;width:1200px;height:746px;background:var(--light)}
.center-kicker{position:absolute;left:0;width:1200px;text-align:center;font-size:14px;color:var(--muted)}
.center-title{position:absolute;left:0;width:1200px;text-align:center;font-size:34px;font-weight:600}
.timeline-line{position:absolute;left:599px;top:2063px;width:2px;height:470px;background:var(--blue)}
.step{position:absolute;left:570px;width:58px;height:58px;border-radius:50%;border:2px solid var(--blue);background:#fff;display:flex;align-items:center;justify-content:center}
.entry{position:absolute;width:400px}
.entry h4{font-size:16px;font-weight:600;margin-bottom:8px}
.entry p{font-size:10px;line-height:17px;color:var(--muted)}
.entry.left{left:130px;text-align:right}
.entry.right{left:670px}

/* contact */
.contact{position:absolute;top:2623px;left:0;width:1200px;height:433px;background:var(--blue-band)}
.contact .center-kicker,.contact .center-title{color:#fff}
.field{position:absolute;color:#fff;font-size:10px;font-weight:700;border-bottom:1px solid rgba(255,255,255,.75)}
.submit{position:absolute;left:512px;top:341px;width:176px;height:39px;background:#fff;color:var(--ink);font-size:11px;font-weight:800;display:flex;align-items:center;justify-content:center;text-transform:uppercase}

/* outcome */
.feature{position:absolute;width:300px;text-align:center}
.feature .ring{width:116px;height:116px;border-radius:50%;background:var(--blue);margin:0 auto;display:flex;align-items:center;justify-content:center;box-shadow:0 0 0 4px #d8eff9}
.feature h4{font-size:16px;font-weight:600;margin-top:28px}
.feature p{font-size:11px;line-height:18px;color:var(--muted);margin:6px auto 0;width:250px}
.brand-btn{position:absolute;top:3680px;width:134px;height:38px;border-radius:8px 0 8px 0;color:#fff;font-size:11px;font-weight:700;display:flex;align-items:center;justify-content:center}

/* faulty */
.faulty{position:absolute;top:3760px;left:0;width:1200px;height:290px}
.faulty h2{position:absolute;top:88px;width:1200px;text-align:center;color:#fff;font-size:32px;font-weight:600}
.faulty .tag{position:absolute;top:135px;width:1200px;text-align:center;color:#fff;font-size:16px;letter-spacing:.5px}
.faulty .btn{left:538px;top:182px;width:128px;height:36px}

/* footer */
.footer{position:absolute;top:4048px;left:0;width:1200px;height:380px;background:var(--footer);color:#cdd3d7}
.footer .brand{position:absolute;left:144px;top:110px;font-size:26px;font-weight:800;color:#fff}
.footer .about{position:absolute;left:129px;top:203px;width:250px;font-size:10px;line-height:18px}
.social{position:absolute;top:274px;width:36px;height:36px;border-radius:50%;border:2px solid #fff}
.footer h5{position:absolute;top:70px;color:var(--blue);font-size:15px;font-weight:600}
.qlinks{position:absolute;left:430px;top:104px;font-size:10px;line-height:24px;list-style:none;color:#fff}
.crow{position:absolute;left:608px;display:flex;gap:10px;font-size:10px;line-height:14px;color:#fff}
.crow .dot{width:26px;height:26px;border-radius:50%;background:var(--blue);display:flex;align-items:center;justify-content:center;flex:none}
.email-in{position:absolute;left:849px;top:107px;width:220px;height:32px;background:#fff;color:#777;font-size:10px;padding:10px 12px}
.sub-btn{position:absolute;left:849px;top:145px;width:220px;height:32px;background:var(--blue);color:#fff;font-size:11px;font-weight:700;display:flex;align-items:center;justify-content:center}
.copy{position:absolute;right:131px;top:282px;font-size:9px;color:#fff}
.copy span{color:var(--blue)}
</style>
</head>
<body>

<div class="topbar">
  <div class="links"><span>PICK-UP ORDER</span><span>|</span><span>ABOUT US</span><span>|</span><span>CONTACT US</span></div>
  <div class="contact"><span>&#9742; +49 4000 555 120-0</span><span>&#9993; info@lumenfix.example</span><span>En ▾</span></div>
</div>

<header class="nav">
  <div class="brand">LumenFix</div>
  <nav class="menu">
    <span class="active">Home</span><span>Endoscope Repair</span><span>Used Endoscopes</span><span>Endoscopy Systems</span><span>Endoscopy Accessories</span><span>Purchase</span>
  </nav>
</header>

<section class="hero">
  <div class="hero-photo" role="img" aria-label="Photo of an endoscope control body on a blue-tinted background"></div>
  <div class="pre">Put Your</div>
  <h1>Endoscope In<br>Reliable Hands!</h1>
  <div class="btn">Get Started</div>
  <div class="mark">LumenFix</div>
  <svg width="1200" height="120" viewBox="0 0 1200 120">
    <path d="M0 60 C 200 20 400 90 650 80 C 900 70 1050 30 1200 40 L1200 120 L0 120 Z" fill="var(--blue)"/>
    <path d="M0 80 C 220 40 420 110 660 98 C 900 86 1060 52 1200 60 L1200 120 L0 120 Z" fill="#fff"/>
  </svg>
</section>

<section class="welcome">
  <div class="welcome-photo" role="img" aria-label="Photo of an endoscopy video processor with a touch screen"></div>
  <div class="kicker">Welcome To</div>
  <h2>LumenFix</h2>
  <p>GmbH is specialized in repairing and saling flexible endoscopes along with accessories and consumables. We offer endoscopes, processors, light sources, accessories and much more – with a focus on the manufacturers Orbica, Pentrel and Fujora.</p>
  <div class="btn">About Us</div>
</section>

<section class="band">
  <div class="band-photo" role="img" aria-label="Photo of several flexible endoscopes laid side by side"></div>
  <div class="kicker">Endoscope repairs and</div>
  <h2>Second hand endoscopes<br>from LumenFix</h2>
  <div class="cause">CAUSE THE OUTCOME MATTERS!</div>
  <p>LumenFix is a privileged partner for the start-up facility or optimisation of existing healthcare facilities, doctor's offices and hospitals. The quality and reliability of our products and our offered service are our best advertisement!</p>
  <div class="btn">About Us</div>
</section>

<div class="card framed" style="left:129px">
  <svg width="46" height="42" viewBox="0 0 46 42" fill="none" stroke="#333" stroke-width="1.6"><circle cx="20" cy="18" r="13"/><path d="M14 14h12M14 19h12M14 24h8"/><rect x="20" y="28" width="20" height="9" rx="3" stroke="var(--blue)"/></svg>
  <h3>Repair</h3><div class="sub">Endoscope repair service</div>
  <p>Manufacturer-independent we repair and maintain endoscopes, individual components (e.g. processors or light sources)...</p>
  <div class="btn">Repair Request</div>
</div>
<div class="card shadow" style="left:450px">
  <svg width="46" height="42" viewBox="0 0 46 42" fill="none" stroke="#333" stroke-width="1.6"><path d="M8 30 L28 8 L38 16 L18 38 Z"/><circle cx="33" cy="8" r="3"/><path d="M14 26l4-2 3 4 4-8" stroke="var(--blue)"/></svg>
  <h3>Sale</h3><div class="sub">Used endoscopes</div>
  <p>Our regular stock includes refurbished gastroscopes, coloscopes, bronchoscopes, cystoscopes....</p>
  <div class="btn">Purchase Request</div>
</div>
<div class="card framed" style="left:770px">
  <svg width="46" height="42" viewBox="0 0 46 42" fill="none" stroke="#333" stroke-width="1.6"><rect x="8" y="12" width="22" height="26" rx="3"/><path d="M14 12c0-6 10-6 10 0"/><path d="M22 24l12-12 6 6-12 12z" stroke="var(--blue)"/></svg>
  <h3>Purchase</h3><div class="sub">Used endoscopes</div>
  <p>We are very interested in buying your old endoscopes – even defective and dismantled! We offer fair conditions! Please contact us...</p>
  <div class="btn">Sell Request</div>
</div>

<section class="decision"></section>
<div class="center-kicker" style="top:1928px">LumenFix GmbH</div>
<div class="center-title" style="top:1948px">Your Decision for your Future</div>
<div class="timeline-line"></div>

<div class="step" style="top:2034px"><svg width="26" height="26" viewBox="0 0 26 26" fill="none" stroke="var(--blue-deep)" stroke-width="1.6"><circle cx="13" cy="13" r="6"/><path d="M13 2v4M13 20v4M2 13h4M20 13h4M5 5l3 3M18 18l3 3M21 5l-3 3M5 21l3-3"/></svg></div>
<div class="step" style="top:2127px"><svg width="26" height="26" viewBox="0 0 26 26" fill="none" stroke="var(--blue-deep)" stroke-width="1.6"><ellipse cx="10" cy="7" rx="6" ry="3"/><path d="M4 7v12c0 2 12 2 12 0V7M4 13c0 2 12 2 12 0"/><path d="M19 18V6l4 4" stroke="var(--blue)"/></svg></div>
<div class="step" style="top:2221px"><svg width="26" height="26" viewBox="0 0 26 26" fill="none" stroke="var(--blue-deep)" stroke-width="1.6"><circle cx="13" cy="13" r="10"/><path d="M13 7v6l4 3"/></svg></div>
<div class="step" style="top:2316px"><svg width="26" height="26" viewBox="0 0 26 26" fill="none" stroke="var(--blue-deep)" stroke-width="1.6"><rect x="4" y="4" width="12" height="10"/><path d="M2 20h8l6-3h6M8 9h4"/></svg></div>
<div class="step" style="top:2409px"><svg width="26" height="26" viewBox="0 0 26 26" fill="none" stroke="var(--blue-deep)" stroke-width="1.6"><path d="M4 22L16 10M18 4a5 5 0 1 0 4 4l-4 1-1-4z"/><path d="M4 4l18 18" stroke="var(--blue)"/></svg></div>
<div class="step" style="top:2503px"><svg width="26" height="26" viewBox="0 0 26 26" fill="none" stroke="var(--blue-deep)" stroke-width="1.6"><circle cx="11" cy="15" r="6"/><circle cx="11" cy="15" r="2"/><circle cx="20" cy="7" r="3" stroke="var(--blue)"/></svg></div>

<div class="entry left" style="top:2024px;left:130px"><h4>Fast Repairs</h4><p>Keep potential disruptions in your doctor's office or in your hospital at minimum as a result of optimized processes and highly qualified specialists in our company</p></div>
<div class="entry right" style="top:2118px"><h4>Highly cost Efficient</h4><p>Benefit from our first class recommendations and implementation by our experienced staff. Our goals is to find the best solutions together with you at the best lowest price point.</p></div>
<div class="entry left" style="top:2212px"><h4>On-site service</h4><p>We will gladly pay you a visit to to carry out analysis and repairs on site. Due to our many years of experience – it doesn't get any faster (whileithin a 250 km range)</p></div>
<div class="entry right" style="top:2314px"><h4>Loan equipment service</h4><p>Use our service of high-quality loan devices during the downtime of your defective endoscope (limited to stock)</p></div>
<div class="entry left" style="top:2408px"><h4>Without a maintenance contract</h4><p>No subscription or other maintenance contract, but one-time and sustainable repair work</p></div>
<div class="entry right" style="top:2512px"><h4>First class Service</h4><p>Our clients always come first!</p></div>

<section class="contact">
  <div class="center-kicker" style="top:50px">Contact Us</div>
  <div class="center-title" style="top:70px">How Can We help You?</div>
  <div class="field" style="left:287px;top:144px;width:305px;height:20px">Name:</div>
  <div class="field" style="left:607px;top:144px;width:306px;height:20px">Phone:</div>
  <div class="field" style="left:287px;top:199px;width:626px;height:20px">Email:</div>
  <div class="field" style="left:287px;top:254px;width:626px;height:70px">Comments:</div>
  <div class="submit">Submit</div>
</section>

<div class="center-kicker" style="top:3124px">Cause The</div>
<div class="center-title" style="top:3143px">Outcome Matters!</div>

<div class="feature" style="left:130px;top:3201px">
  <div class="ring"><svg width="60" height="60" viewBox="0 0 60 60" fill="none" stroke="#fff" stroke-width="2"><circle cx="30" cy="30" r="24"/><circle cx="22" cy="26" r="6"/><circle cx="38" cy="26" r="6"/><path d="M12 44c3-8 17-8 20 0M28 44c3-8 17-8 20 0"/></svg></div>
  <h4>One Company For Everyone</h4><p>We are a service provider for doctors and hospitals!</p>
</div>
<div class="feature" style="left:450px;top:3201px">
  <div class="ring"><svg width="60" height="60" viewBox="0 0 60 60" fill="none" stroke="#fff" stroke-width="2"><circle cx="30" cy="34" r="12"/><circle cx="30" cy="31" r="4"/><path d="M23 42c2-5 12-5 14 0"/><path d="M16 14l2 4 4 0-3 3 1 4-4-2-4 2 1-4-3-3 4 0zM30 8l2 4 4 0-3 3 1 4-4-2-4 2 1-4-3-3 4 0zM44 14l2 4 4 0-3 3 1 4-4-2-4 2 1-4-3-3 4 0z"/></svg></div>
  <h4>Experience Characterises Us</h4><p>We are a service provider for doctors and hospitals!</p>
</div>
<div class="feature" style="left:770px;top:3201px">
  <div class="ring"><svg width="60" height="60" viewBox="0 0 60 60" fill="none" stroke="#fff" stroke-width="2"><rect x="10" y="12" width="40" height="28"/><rect x="22" y="18" width="16" height="16"/><path d="M24 40v8M36 40v8M18 48h24"/></svg></div>
  <h4>The Product Is Close To Our Hearts</h4><p>We are a service provider for doctors and hospitals!</p>
</div>
<div class="feature" style="left:130px;top:3430px">
  <div class="ring"><svg width="60" height="60" viewBox="0 0 60 60" fill="none" stroke="#fff" stroke-width="2"><circle cx="30" cy="26" r="14"/><path d="M23 26l5 5 9-9"/><path d="M20 36l-6 14 7-3 4 6 5-11M40 36l6 14-7-3-4 6-5-11"/></svg></div>
  <h4>Guaranteed Service</h4><p>We are a service provider for doctors and hospitals!</p>
</div>
<div class="feature" style="left:450px;top:3430px">
  <div class="ring"><svg width="60" height="60" viewBox="0 0 60 60" fill="none" stroke="#fff" stroke-width="2"><circle cx="22" cy="36" r="10"/><circle cx="38" cy="24" r="10"/><path d="M17 36h10M22 31v10M33 24h10M22 12v12l-4-4M38 48V36l4 4"/></svg></div>
  <h4>Quality Not Quantity</h4><p>We are a service provider for doctors and hospitals!</p>
</div>
<div class="feature" style="left:770px;top:3430px">
  <div class="ring"><svg width="60" height="60" viewBox="0 0 60 60" fill="none" stroke="#fff" stroke-width="2"><circle cx="30" cy="20" r="8"/><path d="M10 30v12l10 8h6M50 30v12l-10 8h-6M20 36l8 6M40 36l-8 6"/></svg></div>
  <h4>Services For Everyone</h4><p>We are a service provider for doctors and hospitals!</p>
</div>

<div class="brand-btn" style="left:385px;background:var(--orbica)">ORBICA</div>
<div class="brand-btn" style="left:533px;background:var(--pentrel)">PENTREL</div>
<div class="brand-btn" style="left:679px;background:var(--fujora)">FUJORA</div>

<section class="faulty">
  <svg class="abs" style="left:0;top:0" width="1200" height="290" viewBox="0 0 1200 290">
    <path d="M0 22 C 250 0 450 30 700 24 C 900 18 1050 0 1200 10 L1200 290 L0 290 Z" fill="var(--blue-band)"/>
  </svg>
  <h2>Faulty Endoscope?</h2>
  <div class="tag">WE ENSURE QUICK AND SMOOTH REPAIRS!</div>
  <div class="btn">Pick Up Order</div>
</section>

<footer class="footer">
  <div class="brand">LumenFix</div>
  <p class="about">LumenFix GmbH is specialised in the repair and sale of Orbica, Pentrel and Fujora flexible medical endoscopes.</p>
  <div class="social" style="left:130px"></div>
  <div class="social" style="left:181px"></div>

  <h5 style="left:430px">Quick Links</h5>
  <ul class="qlinks"><li>Home</li><li>Endoscope Repair</li><li>Used Endoscopes</li><li>Endoscopy Systems</li><li>Endoscopy Accessories</li><li>Purchase</li></ul>

  <h5 style="left:608px">Contacts</h5>
  <div class="crow" style="top:106px"><div class="dot"><svg width="12" height="14" viewBox="0 0 12 14"><path d="M6 0a5 5 0 0 1 5 5c0 4-5 9-5 9S1 9 1 5a5 5 0 0 1 5-5z" fill="#fff"/><circle cx="6" cy="5" r="2" fill="var(--blue)"/></svg></div><div>Talweg 12<br>20095 Nordhafen, Germany</div></div>
  <div class="crow" style="top:152px"><div class="dot"><svg width="12" height="12" viewBox="0 0 12 12"><path d="M2 1l3 0 1 3-2 1c1 2 2 3 4 4l1-2 3 1v3c-6 0-10-4-10-10z" fill="#fff"/></svg></div><div style="padding-top:6px">+49 4000 555 120-0</div></div>
  <div class="crow" style="top:188px"><div class="dot"><svg width="12" height="10" viewBox="0 0 12 10"><rect x="0" y="0" width="12" height="10" fill="#fff"/><path d="M0 0l6 5 6-5" stroke="var(--blue)" fill="none"/></svg></div><div style="padding-top:6px">info@lumenfix.example</div></div>

  <h5 style="left:849px">Newsletter</h5>
  <div class="email-in">Enter Your Email</div>
  <div class="sub-btn">SUBSCRIBE</div>

  <div class="copy">Copyright © 2022 <span>LumenFix</span>. All Rights Reserved.</div>
</footer>

</body>
</html>
```